SUMMIT GATHERING 2021. August 20th -22nd.

The Hosts of the conference: Grace Tabernacle-Pastors Ron n Della ( Picture with two persons)

Guest Minister: Bishop Lucinda Okotieno. (Cedar Ridge Awakening)

Venue:
Sealand Gateway Lodgeview. 4817 North 239th Avenue Seattle, WA 98174.

Conference times.
Friday August 20th 6pm-8:30pm
Saturday August 21st. 6pm-8:30pm

Sunday August 22nd 10am-1pm
“ CHURCH RENEWAL GATHERING”

5pm-7:30pm
TWOFOLD SURGE GATHERING.

Target Market(s)

18-55

Industry/Entity Type

Religious/ Entertainment.

Requirements
Must have
• A highlight of the Relaunch service on Sunday August 22nd 5pm-7:30pm.
Nice to have
• Excellent ideas….

```html
<!DOCTYPE html>
<html lang="en">
<head>
<meta charset="utf-8">
<title>Summit Gathering – Grace Tabernacle</title>
<link href="https://fonts.googleapis.com/css2?family=Oswald:wght@500;600&family=Didact+Gothic&family=Great+Vibes&family=Mulish:ital,wght@0,400;0,800;1,400&display=swap" rel="stylesheet">
<style>
  :root {
    --page: #efe9e2;
    --sky-deep: #17a3d4;
    --sky-light: #c4e9f2;
    --sand: #f3d6a6;
    --sand-deep: #f1b46c;
    --brown: #5a3413;
    --peach: #fccc95;
    --peach-text: #f7b774;
    --ring-blue: #1a80b1;
    --ink: #1c1a17;
    --col-blue: #a6d8e6;
  }
  * { margin: 0; padding: 0; box-sizing: border-box; }
  html, body { width: 1200px; height: 1200px; overflow: hidden; background: var(--page); }
  .flyer {
    position: absolute; left: 160px; top: 31px; width: 880px; height: 1137px; overflow: hidden;
    background:
      radial-gradient(ellipse 340px 300px at 50% 33%, rgba(255,255,255,.95), rgba(255,255,255,0) 70%),
      linear-gradient(180deg, var(--sky-deep) 0%, var(--sky-light) 42%, #e9ebd8 58%, var(--sand) 72%, var(--sand-deep) 100%);
    box-shadow: 0 8px 24px rgba(0,0,0,.25);
    font-family: "Didact Gothic", sans-serif;
  }
  .abs { position: absolute; }
  .ring { position: absolute; left: 0; top: 0; }
  .service-tag {
    left: 131px; top: 161px; width: 502px; height: 47px; background: var(--peach);
    color: var(--brown); font-family: "Oswald", sans-serif; font-weight: 600; font-size: 35px;
    line-height: 47px; text-align: center; letter-spacing: .5px;
  }
  .title-main {
    left: 128px; top: 190px; width: 510px; text-align: center;
    font-family: "Didact Gothic", sans-serif; font-size: 138px; line-height: 1; letter-spacing: -2px;
    background: linear-gradient(90deg, #6fc8ee 0%, #d9f1f8 35%, #fbe2bd 60%, #f6c07a 100%);
    -webkit-background-clip: text; background-clip: text; color: transparent;
    -webkit-text-stroke: 2.5px #3a3a3a;
  }
  .title-script {
    left: 270px; top: 285px; width: 460px; text-align: center;
    font-family: "Great Vibes", cursive; font-size: 112px; line-height: 1;
    color: #f6c26c; -webkit-text-stroke: 1.5px #d9962e;
  }
  .date-line {
    left: 128px; top: 416px; width: 461px; height: 28px;
    border-top: 1px solid var(--ring-blue); border-bottom: 1px solid var(--ring-blue);
    font-family: "Mulish", sans-serif; font-weight: 800; font-size: 25px; line-height: 26px;
    color: var(--ink); text-align: center; white-space: nowrap;
  }
  .date-line sup { font-size: 13px; }
  .host-column {
    left: 280px; top: 462px; width: 309px; height: 608px;
    border: 6px solid var(--brown); border-top: none;
    background: linear-gradient(180deg, rgba(166,216,230,0) 0%, rgba(166,216,230,.55) 40%, var(--col-blue) 100%);
  }
  .host-photo {
    left: 359px; top: 501px; width: 162px; height: 344px;
    background: linear-gradient(160deg, #3b2aa0 0%, #b23a9d 20%, #dcdad8 55%, #6b4a36 100%);
  }
  .host-caption { left: 280px; top: 862px; width: 309px; text-align: center; color: var(--ink); }
  .host-caption .lead { font-size: 18px; }
  .host-caption .names { font-family: "Mulish", sans-serif; font-weight: 800; font-size: 20px; line-height: 24px; }
  .church-mark {
    left: 280px; top: 985px; width: 309px; text-align: center;
    font-family: "Mulish", sans-serif; font-weight: 800; font-size: 14px; color: var(--brown);
    display: flex; align-items: center; justify-content: center; gap: 6px;
  }
  .church-mark .square { width: 12px; height: 12px; background: var(--brown); }
  .info-box {
    top: 633px; height: 294px; background: var(--brown); color: #fff; text-align: center;
  }
  .info-box::after {
    content: ""; position: absolute; inset: 7px; border: 1px dotted rgba(255,255,255,.7);
  }
  .info-box.left { left: 54px; width: 226px; padding-top: 33px; }
  .info-box.left::after { right: 0; border-right: none; }
  .info-box.right { left: 589px; width: 236px; padding-top: 42px; }
  .info-box.right::after { left: 0; border-left: none; }
  .label { font-family: "Mulish", sans-serif; font-weight: 800; color: var(--peach-text); font-size: 20px; line-height: 24px; }
  .body-text { font-size: 19px; line-height: 23px; }
  .note { font-family: "Mulish", sans-serif; font-style: italic; font-size: 14px; line-height: 18px; }
  .address { font-size: 16px; line-height: 21px; }
  .gap { height: 32px; }
  .schedule .day { font-family: "Mulish", sans-serif; font-weight: 800; color: var(--peach-text); font-size: 17px; line-height: 21px; }
  .schedule .time { font-size: 17px; line-height: 21px; }
  .highlight-time { font-size: 21px; line-height: 26px; margin-top: 26px; }
  .highlight-name { font-family: "Mulish", sans-serif; font-weight: 800; color: var(--peach-text); font-size: 19px; line-height: 25px; }
</style>
</head>
<body>
<main class="flyer">
  <svg class="ring" width="880" height="1137" viewBox="0 0 880 1137" aria-hidden="true">
    <g transform="rotate(-8 439 318)">
      <ellipse cx="439" cy="318" rx="382" ry="192" fill="none" stroke="var(--ring-blue)" stroke-width="14"/>
      <ellipse cx="439" cy="318" rx="370" ry="182" fill="none" stroke="var(--brown)" stroke-width="7"/>
    </g>
  </svg>

  <div class="abs service-tag">CHURCH RENEWAL GATHERING</div>
  <h1 class="abs title-main">SUMMIT</h1>
  <div class="abs title-script">Gathering</div>
  <div class="abs date-line">Sunday August 22<sup>nd</sup> 10am – 1pm</div>

  <div class="abs host-column"></div>
  <div class="abs host-photo" role="img" aria-label="Photo of the hosting pastors, Ron and Della"></div>
  <div class="abs host-caption">
    <p class="lead">The Hosts of the conference</p>
    <p class="names">Grace Tabernacle Pastors<br>Ron and Della</p>
  </div>
  <div class="abs church-mark"><span class="square"></span>Grace Tabernacle</div>

  <section class="abs info-box left">
    <p class="label">Guest minister</p>
    <p class="body-text">Bishop<br>Lucinda Okotieno</p>
    <p class="note">(Cedar Ridge Awakening)</p>
    <div class="gap"></div>
    <p class="label">Venue</p>
    <p class="address">Sealand Gateway<br>Lodgeview. 4817 North<br>239th Avenue Seattle,<br>WA 98174</p>
  </section>

  <section class="abs info-box right schedule">
    <p class="day">Friday August 20th</p>
    <p class="time">6:00pm – 8:30pm</p>
    <p class="day">Saturday August 21st</p>
    <p class="time">6:00pm – 8:30pm</p>
    <p class="highlight-time">5pm – 7:30pm</p>
    <p class="highlight-name">TWOFOLD SURGE<br>GATHERING</p>
  </section>
</main>
</body>
</html>
```